Business Consulting Business Card

professional business card with basic information (1) First and Last name (2) email address, (3) phone number, (4) website.

```html
<!DOCTYPE html>
<html lang="en">
<head>
<meta charset="utf-8">
<title>Bay Meadow Business Card</title>
<link rel="stylesheet" href="https://fonts.googleapis.com/css2?family=Montserrat:wght@400;500;800&family=Open+Sans:wght@400;600&display=swap">
<style>
  :root {
    --navy: #03283f;
    --navy-ink: #0d2a3d;
    --teal: #3fb3c4;
    --paper: #ffffff;
    --stage: #e9ebee;
    --muted: #2b3b47;
  }
  * { box-sizing: border-box; margin: 0; padding: 0; }
  html, body { width: 1200px; height: 900px; overflow: hidden; }
  body {
    background: var(--stage);
    font-family: "Open Sans", Arial, sans-serif;
    position: relative;
  }
  .card {
    position: absolute;
    left: 320px;
    width: 560px;
    height: 320px;
    box-shadow: 0 6px 18px rgba(0,0,0,0.12);
  }
  .card-front { top: 110px; background: var(--paper); }
  .card-back { top: 470px; background: var(--navy); }

  .brand {
    position: absolute;
    display: flex;
    align-items: center;
    gap: 14px;
  }
  .brand-dot {
    width: 34px; height: 34px;
    border-radius: 50%;
    background: var(--teal);
    flex: none;
  }
  .brand-name {
    font-family: "Montserrat", Arial, sans-serif;
    font-weight: 500;
    letter-spacing: 0.28em;
    white-space: nowrap;
  }
  .card-front .brand { left: 34px; top: 143px; }
  .card-front .brand-name { font-size: 17px; color: var(--navy-ink); }

  .divider {
    position: absolute;
    left: 282px; top: 60px;
    width: 2px; height: 210px;
    background: var(--navy-ink);
  }
  .identity { position: absolute; left: 310px; top: 58px; }
  .person-name {
    font-family: "Montserrat", Arial, sans-serif;
    font-size: 21px;
    color: var(--navy-ink);
    line-height: 1.1;
    white-space: nowrap;
  }
  .person-name .first { font-weight: 800; }
  .person-name .last { font-weight: 400; }
  .person-title {
    font-size: 13px;
    color: var(--muted);
    margin-top: 2px;
  }
  .contact-list {
    list-style: none;
    position: absolute;
    left: 310px; top: 136px;
  }
  .contact-item {
    display: flex;
    align-items: center;
    gap: 12px;
    height: 30px;
    font-size: 12.5px;
    color: var(--navy-ink);
    white-space: nowrap;
  }
  .contact-icon {
    width: 22px; height: 22px;
    border-radius: 50%;
    background: var(--navy-ink);
    display: flex; align-items: center; justify-content: center;
    flex: none;
  }
  .contact-icon svg { width: 12px; height: 12px; }

  .card-back .brand {
    left: 50%; top: 118px;
    transform: translateX(-50%);
    gap: 22px;
  }
  .card-back .brand-dot { width: 52px; height: 52px; background: var(--paper); }
  .card-back .brand-name { font-size: 26px; color: var(--paper); }
  .back-web {
    position: absolute;
    left: 0; right: 0; bottom: 26px;
    display: flex; justify-content: center; align-items: center;
    gap: 10px;
    color: var(--paper);
    font-size: 15px;
  }
  .back-web svg { width: 18px; height: 18px; }
</style>
</head>
<body>

<section class="card card-front" aria-label="Card front">
  <div class="brand">
    <span class="brand-dot"></span>
    <span class="brand-name">BAY MEADOW</span>
  </div>
  <div class="divider"></div>
  <div class="identity">
    <p class="person-name"><span class="first">DANA</span> <span class="last">WHITFIELD</span></p>
    <p class="person-title">General Manager</p>
  </div>
  <ul class="contact-list">
    <li class="contact-item">
      <span class="contact-icon"><svg viewBox="0 0 24 24" fill="none" stroke="#fff" stroke-width="2" stroke-linecap="round" stroke-linejoin="round"><path d="M22 16.9v3a2 2 0 0 1-2.2 2 19.8 19.8 0 0 1-8.6-3.1 19.5 19.5 0 0 1-6-6A19.8 19.8 0 0 1 2.1 4.2 2 2 0 0 1 4.1 2h3a2 2 0 0 1 2 1.7c.1.9.4 1.8.7 2.7a2 2 0 0 1-.5 2.1L8 9.8a16 16 0 0 0 6 6l1.3-1.3a2 2 0 0 1 2.1-.4c.9.3 1.8.6 2.7.7a2 2 0 0 1 1.7 2z"/></svg></span>
      <span>+111 24680 1357</span>
    </li>
    <li class="contact-item">
      <span class="contact-icon"><svg viewBox="0 0 24 24" fill="none" stroke="#fff" stroke-width="2" stroke-linejoin="round"><rect x="3" y="5" width="18" height="14" rx="1"/><path d="M3 6l9 7 9-7"/></svg></span>
      <span>hello@baymeadow.com</span>
    </li>
    <li class="contact-item">
      <span class="contact-icon"><svg viewBox="0 0 24 24" fill="none" stroke="#fff" stroke-width="2" stroke-linecap="round"><rect x="6" y="3" width="12" height="18" rx="6"/><path d="M12 7v4"/></svg></span>
      <span>www.baymeadow.com</span>
    </li>
    <li class="contact-item">
      <span class="contact-icon"><svg viewBox="0 0 24 24" fill="none" stroke="#fff" stroke-width="2"><path d="M12 22s7-7 7-12a7 7 0 0 0-14 0c0 5 7 12 7 12z"/><circle cx="12" cy="10" r="2.5"/></svg></span>
      <span>Street Address Here</span>
    </li>
  </ul>
</section>

<section class="card card-back" aria-label="Card back">
  <div class="brand">
    <span class="brand-dot"></span>
    <span class="brand-name">BAY MEADOW</span>
  </div>
  <p class="back-web">
    <svg viewBox="0 0 24 24" fill="none" stroke="#fff" stroke-width="1.8"><circle cx="12" cy="12" r="10"/><path d="M2 12h20M12 2c3 3 4 6.5 4 10s-1 7-4 10c-3-3-4-6.5-4-10s1-7 4-10z"/></svg>
    <span>www.baymeadow.com</span>
  </p>
</section>

</body>
</html>
```